TDM accounting firm Canada - Modern and professional business cards

To use our existing logo and create a modern looking business card.
We are looking for double sided style.
Silver-metallic background - our logo in front (reverse side)
The reverse side from the attachment- big logo over silver-metallic background is preferred.
we would like to have a business card template that can be modified to change names, addresses, and other

Industry/Entity Type

Accounting

Contact Information for Business Card

Reverse side silver-metallic finish

Font styles to use
Sans Serif

Requirements
Must have
• Reverse side silver-metallic finish
• Modern look

```html
<!DOCTYPE html>
<html lang="en">
<head>
<meta charset="utf-8">
<title>TDM – Business Card</title>
<link href="https://fonts.googleapis.com/css2?family=Arimo:wght@400;700&display=swap" rel="stylesheet">
<style>
  :root{
    --page:#e9e7e4;
    --ink-dark:#141414;
    --ink-mid:#2a2a2a;
    --silver-1:#8d8d8d;
    --silver-2:#e4e4e4;
    --silver-3:#b3b3b3;
    --text-dark:#3a3a3a;
    --text-light:#f2f2f2;
    --text-muted:#9a9a9a;
  }
  *{box-sizing:border-box;margin:0;padding:0}
  html,body{width:1200px;height:1000px;overflow:hidden;background:var(--page);
    font-family:"Arimo",Arial,sans-serif}
  .card{position:absolute;left:250px;width:700px;height:400px;overflow:hidden;
    box-shadow:0 10px 30px rgba(0,0,0,.35)}
  .card--back{top:60px;background:var(--ink-dark)}
  .card--front{top:530px;background:linear-gradient(135deg,#0f0f0f,#2d2d2d 70%,#3a3a3a)}

  .texture{position:absolute;inset:0;background:radial-gradient(circle at 40% 40%,#262626,#0c0c0c 80%)}
  .silver-band{position:absolute;left:0;right:0;
    background:linear-gradient(100deg,var(--silver-1) 0%,var(--silver-2) 45%,var(--silver-3) 65%,var(--silver-2) 85%,var(--silver-1) 100%)}
  .card--back .silver-band{top:115px;height:130px}

  .lockup{position:absolute;display:flex;align-items:center;gap:18px}
  .lockup__mark{display:flex;flex-direction:column;align-items:center}
  .lockup__name{font-weight:700;font-size:58px;letter-spacing:2px;line-height:1}
  .lockup__tag{font-weight:700;font-size:11px;letter-spacing:1.5px;margin-top:4px}
  .lockup__rule{width:2px;height:62px}
  .lockup__company{font-weight:700;font-size:20px;line-height:1.02;letter-spacing:1.5px;text-transform:uppercase}

  .card--back .lockup{left:150px;top:145px}
  .card--back .lockup__name,.card--back .lockup__tag,.card--back .lockup__company{color:var(--ink-mid)}
  .card--back .lockup__rule{background:var(--ink-mid)}
  .url{position:absolute;font-weight:700;font-size:17px}
  .card--back .url{left:0;right:0;top:300px;text-align:center;color:var(--text-light)}

  .card--front .lockup{left:60px;top:60px}
  .card--front .lockup__name,.card--front .lockup__tag{color:var(--silver-2)}
  .card--front .lockup__company{color:var(--silver-3)}
  .card--front .lockup__rule{background:var(--silver-3)}
  .card--front .silver-band{top:190px;bottom:0}
  .divider{position:absolute;left:0;right:0;height:3px;background:#555}
  .divider--top{top:186px;background:#6a6a6a}
  .divider--mid{top:292px;height:2px;background:#7d7d7d}
  .person{position:absolute;left:55px;top:212px;color:var(--text-dark)}
  .person__name{font-weight:700;font-size:26px}
  .person__title{font-size:13px;letter-spacing:1px;margin-top:8px;color:#555}
  .card--front .url{right:40px;top:228px;color:var(--text-dark)}
  .contacts{position:absolute;left:55px;top:305px;list-style:none;color:var(--text-dark);font-weight:700;font-size:18px}
  .contacts li{display:flex;align-items:center;gap:18px;height:28px}
  .contacts svg{width:20px;height:20px;fill:#2a2a2a}
</style>
</head>
<body>
  <section class="card card--back">
    <div class="texture" role="img" aria-label="Dark hexagonal mesh texture"></div>
    <div class="silver-band"></div>
    <div class="lockup">
      <div class="lockup__mark">
        <span class="lockup__name">TDM</span>
        <span class="lockup__tag">SR&amp;ED · TAX · ACCOUNTING</span>
      </div>
      <div class="lockup__rule"></div>
      <div class="lockup__company">Northfield<br>Professional<br>Corporation</div>
    </div>
    <p class="url">www.tdm-cpa.com</p>
  </section>

  <section class="card card--front">
    <div class="lockup">
      <div class="lockup__mark">
        <span class="lockup__name">TDM</span>
        <span class="lockup__tag">SR&amp;ED · TAX · ACCOUNTING</span>
      </div>
      <div class="lockup__rule"></div>
      <div class="lockup__company">Northfield<br>Professional<br>Corporation</div>
    </div>
    <div class="silver-band"></div>
    <div class="divider divider--top"></div>
    <div class="person">
      <h1 class="person__name">Marco Delgado CPA, CGA.</h1>
      <p class="person__title">PRINCIPAL AND SENIOR CONSULTANT</p>
    </div>
    <p class="url">www.tdm-cpa.com</p>
    <div class="divider divider--mid"></div>
    <ul class="contacts">
      <li><svg viewBox="0 0 20 20"><rect x="5" y="1" width="10" height="18" rx="2"/><rect x="7" y="4" width="6" height="10" fill="#ccc"/></svg>(555) 214-3086</li>
      <li><svg viewBox="0 0 20 20"><path d="M2 7c0-3 16-3 16 0v2h-4V7H6v2H2z"/><rect x="4" y="10" width="12" height="8" rx="1"/></svg>(555) 907-1482</li>
      <li><svg viewBox="0 0 20 20"><rect x="1" y="4" width="18" height="12"/><path d="M1 4l9 7 9-7" stroke="#ccc" stroke-width="1.5" fill="none"/></svg>marco@tdm-cpa.com</li>
    </ul>
  </section>
</body>
</html>
```